Brisca Coffee Cups

We already have Brisca Coffee cups, but the existing design is dated.
It needs a fresh modern look. (this look will be used with all Brisca advertising..
But the look and font of the word Brisca needs to say the same.

Industry/Entity Type

Advertising

```html
<!DOCTYPE html>
<html lang="en">
<head>
<meta charset="utf-8">
<title>Brisca Coffee Packaging</title>
<link rel="stylesheet" href="https://fonts.googleapis.com/css2?family=Open+Sans:wght@600;700&display=swap">
<style>
  :root {
    --backdrop: #c8c8c5;
    --paper: #ecebe8;
    --espresso: #2e1710;
    --mocha: #5a3a30;
    --cinnamon: #8a5845;
    --latte: #a39893;
    --ink: #3a1f14;
  }
  * { box-sizing: border-box; margin: 0; padding: 0; }
  html, body { width: 1000px; height: 1200px; overflow: hidden; }
  body {
    background: var(--backdrop);
    font-family: "Open Sans", Arial, sans-serif;
    position: relative;
  }
  .divider {
    position: absolute; left: 0; top: 545px; width: 1000px; height: 2px;
    background: #d6d6d3;
  }
  .panel {
    position: absolute;
    display: flex; flex-direction: column;
    background: var(--paper);
    box-shadow: 0 6px 14px rgba(0,0,0,0.12);
  }
  .pattern-band {
    background: linear-gradient(90deg, var(--espresso), var(--mocha) 30%, var(--cinnamon) 55%, var(--latte) 75%, var(--mocha));
  }
  .label-band {
    display: flex; flex-direction: column; align-items: center; justify-content: center;
    background: var(--paper);
  }
  .web-address {
    color: var(--ink); font-weight: 700; letter-spacing: 0.02em;
  }
  .brand-name {
    color: var(--ink); font-weight: 600; line-height: 1; letter-spacing: 0.01em;
  }
  .lid { background: var(--espresso); }

  /* top row */
  .coffee-bag { left: 40px; top: 30px; width: 220px; height: 440px; }
  .gift-box   { left: 280px; top: 80px; width: 220px; height: 390px; }
  .cup-small  { left: 530px; top: 310px; width: 130px; height: 215px; }
  .cup-medium { left: 680px; top: 270px; width: 135px; height: 255px; }
  .cup-large  { left: 835px; top: 215px; width: 135px; height: 310px; }

  /* feature bag */
  .feature-bag { left: 320px; top: 595px; width: 400px; height: 575px; }
</style>
</head>
<body>

  <!-- coffee bag -->
  <div class="panel coffee-bag">
    <div class="label-band" style="height:85px"><span class="web-address" style="font-size:8px">www.briscacups.com.au</span></div>
    <div class="pattern-band" style="height:85px" role="img" aria-label="Checkered pattern in brown and taupe squares"></div>
    <div class="label-band" style="height:115px"><span class="brand-name" style="font-size:38px">Brisca</span></div>
    <div class="pattern-band" style="flex:1" role="img" aria-label="Checkered pattern in brown and taupe squares"></div>
  </div>

  <!-- gift box -->
  <div class="panel gift-box">
    <div class="pattern-band" style="height:28px" role="img" aria-label="Checkered pattern in brown and taupe squares"></div>
    <div class="label-band" style="height:55px"><span class="web-address" style="font-size:8px">www.briscacups.com.au</span></div>
    <div class="pattern-band" style="height:60px" role="img" aria-label="Checkered pattern in brown and taupe squares"></div>
    <div class="label-band" style="height:110px"><span class="brand-name" style="font-size:38px">Brisca</span></div>
    <div class="pattern-band" style="flex:1" role="img" aria-label="Checkered pattern in brown and taupe squares"></div>
  </div>

  <!-- cups -->
  <div class="panel cup-small">
    <div class="lid" style="height:22px"></div>
    <div class="pattern-band" style="height:25px" role="img" aria-label="Checkered pattern in brown and taupe squares"></div>
    <div class="label-band" style="height:90px">
      <span class="brand-name" style="font-size:27px">Brisca</span>
      <span class="web-address" style="font-size:6px;margin-top:14px">www.briscacups.com.au</span>
    </div>
    <div class="pattern-band" style="flex:1" role="img" aria-label="Checkered pattern in brown and taupe squares"></div>
  </div>

  <div class="panel cup-medium">
    <div class="lid" style="height:30px"></div>
    <div class="pattern-band" style="height:35px" role="img" aria-label="Checkered pattern in brown and taupe squares"></div>
    <div class="label-band" style="height:100px">
      <span class="brand-name" style="font-size:27px">Brisca</span>
      <span class="web-address" style="font-size:6px;margin-top:16px">www.briscacups.com.au</span>
    </div>
    <div class="pattern-band" style="flex:1" role="img" aria-label="Checkered pattern in brown and taupe squares"></div>
  </div>

  <div class="panel cup-large">
    <div class="lid" style="height:35px"></div>
    <div class="pattern-band" style="height:65px" role="img" aria-label="Checkered pattern in brown and taupe squares"></div>
    <div class="label-band" style="height:115px">
      <span class="brand-name" style="font-size:29px">Brisca</span>
      <span class="web-address" style="font-size:6px;margin-top:22px">www.briscacups.com.au</span>
    </div>
    <div class="pattern-band" style="flex:1" role="img" aria-label="Checkered pattern in brown and taupe squares"></div>
  </div>

  <div class="divider"></div>

  <!-- feature bag -->
  <div class="panel feature-bag">
    <div class="pattern-band" style="height:45px" role="img" aria-label="Checkered pattern in brown and taupe squares"></div>
    <div class="label-band" style="height:70px"><span class="web-address" style="font-size:9px">www.briscacups.com.au</span></div>
    <div class="pattern-band" style="height:85px" role="img" aria-label="Checkered pattern in brown and taupe squares"></div>
    <div class="label-band" style="height:170px"><span class="brand-name" style="font-size:52px">Brisca</span></div>
    <div class="pattern-band" style="flex:1" role="img" aria-label="Checkered pattern in brown and taupe squares"></div>
  </div>

</body>
</html>
```